Human Resource Consulting practice needs a business card design

We need a business card design (double sided colour) for our Human Resource (HR) consulting practice in regional New South Wales, australia. Our business name is Staffwise Partners. We support small and medium business across the Mid North Coast of New South Wales by providing them with outsourced HR support, services and products to help them achieve compliance with workplace legislation and across all areas of the employment lifecycle from recruitment to termination and everything in between. Our corporate colours are hot pink and black. The final design should communicate professionalism, trust, people focus.
I have attached the current (old) business card for your reference.

Target Market(s)

Business owners and high level managers

Industry/Entity Type

Business

Contact Information for Business Card

Name
Title
Phone no
Mobile no
Address
PO Box
email address
website

Colors
e34197

Requirements
Must have
• Tempate for changing business card personal details including Name, position title, mobile number, email address.
• Keep current logo and colours as per attached
• Logo must be presented in 2 colours or black only not white
Nice to have
• One side logo and graphic only other side logo and personal details
Should not have
• Should not be the same as the current version (attached) but a modern interpretation.
• Does not need a busy reverse side with our list of services as per current version. I feel this is too busy.
• No photos

```html
<!DOCTYPE html>
<html lang="en">
<head>
<meta charset="utf-8">
<title>Staffwise Partners – Business Card</title>
<link href="https://fonts.googleapis.com/css2?family=Source+Sans+3:wght@400;600&display=swap" rel="stylesheet">
<style>
  :root {
    --hot-pink: #dd1479;
    --backdrop: #ececec;
    --card-white: #ffffff;
    --text-grey: #9a9a9a;
    --icon-grey: #b9b9b9;
    --pattern-grey: #e9e9e9;
  }
  * { margin: 0; padding: 0; box-sizing: border-box; }
  html, body {
    width: 1200px; height: 999px; overflow: hidden;
    background: var(--backdrop);
    font-family: "Source Sans 3", "Myriad Pro", Arial, sans-serif;
  }
  .stage { position: relative; width: 1200px; height: 999px; }

  .card {
    position: absolute; top: 172px;
    width: 372px; height: 650px;
    box-shadow: 0 1px 4px rgba(0,0,0,0.12);
  }
  .card--front { left: 211px; background: var(--hot-pink); }
  .card--back  { left: 618px; background: var(--card-white); overflow: hidden; }

  .brand-tab {
    position: absolute; left: 0; top: 266px;
    width: 274px; height: 118px;
    background: var(--card-white);
    border-radius: 0 12px 12px 0;
    display: flex; align-items: center;
    padding-left: 16px;
  }
  .brand-name {
    color: var(--hot-pink);
    font-weight: 600; font-size: 41px; line-height: 40px;
    letter-spacing: -0.5px;
  }

  .texture-field {
    position: absolute; left: 0; top: 4px;
    width: 272px; height: 350px;
    background: radial-gradient(ellipse at 40% 45%, var(--pattern-grey) 0%, rgba(233,233,233,0.6) 45%, rgba(255,255,255,0) 75%);
  }

  .name-bar {
    position: absolute; left: 0; top: 266px;
    width: 328px; height: 26px;
    background: var(--hot-pink);
    border-radius: 0 3px 3px 0;
  }
  .person-name {
    position: absolute; left: 38px; top: 263px;
    color: var(--card-white); font-size: 26px; line-height: 30px;
  }
  .person-title {
    position: absolute; left: 38px; top: 294px;
    color: var(--text-grey); font-size: 22px; line-height: 26px;
  }

  .contact-list { list-style: none; }
  .contact-item {
    position: absolute; left: 0;
    color: var(--text-grey); font-size: 18px; line-height: 24px;
  }
  .contact-item svg {
    position: absolute; left: 37px; top: 5px;
    width: 16px; height: 16px;
    stroke: var(--icon-grey); fill: none; stroke-width: 1.2;
  }
  .contact-item span { position: absolute; left: 91px; white-space: nowrap; }
  .contact-address { top: 356px; }
  .contact-address-line2 { top: 392px; }
  .contact-phone  { top: 427px; }
  .contact-mobile { top: 457px; }
  .contact-fax    { top: 492px; }
  .contact-email  { top: 527px; }

  .footer-rule {
    position: absolute; left: 0; top: 602px;
    width: 328px; height: 6px; background: var(--hot-pink);
  }
  .footer-rule--thin { top: 611px; height: 2px; }
</style>
</head>
<body>
<main class="stage">

  <section class="card card--front" aria-label="Card front">
    <div class="brand-tab">
      <div class="brand-name">Staffwise<br>Partners</div>
    </div>
  </section>

  <section class="card card--back" aria-label="Card back">
    <div class="texture-field" role="img" aria-label="Soft grey scattered square pixel texture"></div>

    <div class="name-bar"></div>
    <p class="person-name">Megan Holt</p>
    <p class="person-title">Principal Consultant</p>

    <ul class="contact-list">
      <li class="contact-item contact-address">
        <svg viewBox="0 0 16 16"><path d="M2 8 L8 2.5 L14 8 M4 7 V14 H12 V7 M7 14 V10 H9 V14"/></svg>
        <span>PO Box 318, Lakehaven,</span>
      </li>
      <li class="contact-item contact-address-line2"><span>NSW 2441</span></li>
      <li class="contact-item contact-phone">
        <svg viewBox="0 0 16 16"><path d="M2 6 C2 3 14 3 14 6 L12 7 L11 5.5 H5 L4 7 Z M4 8 H12 L13 13 H3 Z"/><circle cx="8" cy="10.5" r="1.3"/></svg>
        <span>02 6500 4127</span>
      </li>
      <li class="contact-item contact-mobile">
        <svg viewBox="0 0 16 16"><rect x="4.5" y="1.5" width="7" height="13" rx="1"/><path d="M7 12.5 H9"/></svg>
        <span>0400 215 386</span>
      </li>
      <li class="contact-item contact-fax">
        <svg viewBox="0 0 16 16"><rect x="2" y="6" width="12" height="8"/><path d="M4 6 V2 H10 V6 M5 9 H7 M5 11 H7 M9 9 H12 M9 11 H12"/></svg>
        <span>02 6500 4190</span>
      </li>
      <li class="contact-item contact-email">
        <svg viewBox="0 0 16 16"><rect x="2" y="4" width="12" height="8"/><path d="M2 4 L8 9 L14 4"/></svg>
        <span>megan@staffwise.com.au</span>
      </li>
    </ul>

    <div class="footer-rule"></div>
    <div class="footer-rule footer-rule--thin"></div>
  </section>

</main>
</body>
</html>
```